BrightPath Vitality Brochure

Creation of a 7-page brochure (including the cover) that will be converted into a digital brochure via .pdf format. We would like to see a design that communicates the technology-forward and ai-powered medical and wellness approach while also communicating the necessary information.
One the catalog is created, we will convert it from a .pdf format to a digitized, flippable catalog so that potential customers can learn more about us. A small scale example of what we are creating is available at the following link: http://pagetrove.example-flip.net/i/2847193-brightpath-vitality-plan-example/0?
This catalog is 7 pages plus the cover page. Our target is men and women over the age of 35 who are looking to improve the quality of their life, not just their lifespan, by getting lab and diagnostics done at BrightPath Vitality and then us providing an integrative wellness solution focused on our TriAxis Method.
The design format is in the Digital Guide.docx document which gives a page by page desired layout. Some supporting images and reference links are included in that brief. We are evaluating the initial layout, look and feel. Once we select a design layout, we will come back with a round of revisions that will include requests where we can add BUTTONS or callouts to click on when it is digitized. So, to the best ability leave a little space on the page for these callouts which can be little buttons to LEARN MORE.

```html
<!DOCTYPE html>
<html lang="en">
<head>
<meta charset="utf-8">
<title>BrightPath Vitality Brochure</title>
<link href="https://fonts.googleapis.com/css2?family=Poppins:wght@500;600;700;800&family=Open+Sans:wght@400;600;700&display=swap" rel="stylesheet">
<style>
:root{
  --green:#3f8a3c;
  --green-dark:#2f6f2d;
  --green-light:#6fae55;
  --cream:#eef2dc;
  --paper:#ffffff;
  --ink:#2b2b2b;
  --muted:#5c5c5c;
  --bg:#d9d9d9;
  --pie-blue:#2f7fc1;
  --pie-yellow:#f2c230;
  --pie-orange:#e0743a;
  --pie-green:#5aa447;
}
*{box-sizing:border-box;margin:0;padding:0}
html,body{width:1200px;height:3000px;overflow:hidden;background:var(--bg)}
body{font-family:"Open Sans",sans-serif;color:var(--ink)}
.canvas{position:relative;width:1200px;height:3000px}
.section{position:relative;height:750px}
.spread{position:absolute;left:60px;top:25px;width:1080px;height:700px;display:flex;box-shadow:0 6px 24px rgba(0,0,0,.18)}
.page{position:relative;width:540px;height:700px;overflow:hidden}
.page--green{background:linear-gradient(150deg,var(--green-light),var(--green) 55%,var(--green-dark))}
.page--cream{background:var(--cream)}
.page--white{background:var(--paper)}
.gutter-shade{position:absolute;left:520px;top:0;width:40px;height:700px;background:linear-gradient(90deg,rgba(0,0,0,0),rgba(0,0,0,.08),rgba(0,0,0,0));pointer-events:none}
.photo{position:absolute;background:linear-gradient(135deg,#c9b59a,#8f7a63 60%,#5d6b54);}
.photo--round{border-radius:50%}
h2,h3,.display{font-family:"Poppins",sans-serif}
.abs{position:absolute}
p{font-size:10.5px;line-height:1.5}

/* cover */
.brand{display:flex;align-items:center;gap:10px;color:#fff;font-family:"Poppins",sans-serif;font-weight:600;font-size:24px}
.brand-dot{width:26px;height:26px;border-radius:50%;background:#fff}
.brand-line{color:#e6f0dc;font-size:10px;letter-spacing:.5px}
.tagline{color:#fff;font-family:"Poppins",sans-serif;font-weight:500;font-size:19px;line-height:1.3}
.site{color:#fff;font-weight:700;font-size:12px}
.deco-circle{position:absolute;border-radius:50%;background:rgba(255,255,255,.07)}
.contact{position:absolute;left:190px;top:210px;width:310px;height:310px;border-radius:50%;background:#fff;display:flex;flex-direction:column;align-items:center;justify-content:center;text-align:center}
.contact h2{font-size:26px;font-weight:600;color:var(--ink)}
.contact-icons{display:flex;gap:10px;margin:12px 0}
.contact-icons span{width:24px;height:24px;border-radius:50%;background:var(--cream);display:flex;align-items:center;justify-content:center}
.contact p{font-size:12px;line-height:1.6}
.contact .web{font-weight:700;margin-top:8px}

/* inside pages */
.title{font-weight:700;font-size:22px;line-height:1.2;color:var(--ink)}
.title em{font-style:normal;color:var(--green)}
.item{position:absolute;display:flex;gap:16px;width:420px}
.icon{flex:none;width:52px;height:52px;border-radius:50%;border:2px solid var(--green);background:#fff;display:flex;align-items:center;justify-content:center}
.icon--solid{background:var(--green);border-color:var(--green)}
.item h3{font-size:17px;font-weight:600;margin-bottom:4px}
.rail{position:absolute;width:2px;background:var(--green)}
.rule{position:absolute;height:1px;background:#b9c9a6}
.panel{position:absolute;background:var(--green);border-radius:18px;color:#fff;padding:24px 26px}
.panel h3{font-size:15px;font-weight:700;line-height:1.3;margin-bottom:10px}
.panel p{color:#eef5e6;margin-bottom:8px}
.panel strong{color:#fff}
.pie-wrap{position:absolute;left:390px;top:290px;width:300px;height:300px;border-radius:50%;background:#fff;box-shadow:0 0 0 1px #e4e8d6}
.pie-label{position:absolute;font-family:"Poppins",sans-serif;font-weight:700;font-size:8.5px;text-align:center;line-height:1.2}
.step{position:absolute;display:flex;gap:10px;width:220px}
.step .icon{width:38px;height:38px}
.step p{font-size:10px}
.book{position:absolute;border-radius:6px}
.faq{display:flex;gap:12px;margin-bottom:18px}
.faq .icon{width:34px;height:34px;background:transparent;border-color:#fff}
.faq h3{font-size:14.5px;margin-bottom:5px}
.faq ul{list-style:none;font-size:10.5px;color:#eef5e6;margin:4px 0}
.faq li::before{content:"\2713  ";font-weight:700}
.faq-heading{font-family:"Poppins",sans-serif;font-weight:800;font-size:44px;line-height:1.1}
.faq-heading span{color:var(--green)}
</style>
</head>
<body>
<div class="canvas">

<!-- Spread 1: back and front cover -->
<section class="section">
  <div class="spread">
    <div class="page page--green">
      <div class="photo photo--round" style="left:-230px;top:150px;width:560px;height:560px;background:linear-gradient(135deg,#e6b887,#a9483f 55%,#6e7fb0)" role="img" aria-label="Photo of a smiling young child in a red jacket"></div>
      <div class="contact">
        <h2>Contact Us</h2>
        <div class="contact-icons">
          <span><svg width="12" height="12" viewBox="0 0 24 24"><path d="M6 3l4 4-2 3c1 2 3 4 5 5l3-2 4 4-3 3C10 20 4 14 3 6z" fill="var(--green)"/></svg></span>
          <span><svg width="12" height="12" viewBox="0 0 24 24"><path d="M12 2a7 7 0 0 0-7 7c0 5 7 13 7 13s7-8 7-13a7 7 0 0 0-7-7zm0 10a3 3 0 1 1 0-6 3 3 0 0 1 0 6z" fill="var(--green)"/></svg></span>
          <span><svg width="12" height="12" viewBox="0 0 24 24"><circle cx="12" cy="12" r="9" fill="none" stroke="var(--green)" stroke-width="2"/><path d="M3 12h18M12 3c3 3 3 15 0 18M12 3c-3 3-3 15 0 18" fill="none" stroke="var(--green)" stroke-width="2"/></svg></span>
        </div>
        <p>(555) 014-2280</p>
        <p>482 Linden Crest Rd,<br>Fairhaven, ST 00412</p>
        <p class="web">www.brightpathvitality.com</p>
      </div>
    </div>
    <div class="page page--green">
      <div class="deco-circle" style="left:-60px;top:80px;width:300px;height:300px"></div>
      <div class="deco-circle" style="left:300px;top:-60px;width:280px;height:280px"></div>
      <div class="abs" style="left:60px;top:60px">
        <div class="brand"><span class="brand-dot"></span>BrightPath Vitality</div>
        <div class="brand-line" style="margin:4px 0 0 36px">Look Good | Feel Good | Be Good</div>
        <div class="tagline" style="margin:16px 0 0 36px">Start Living and Looking<br>Like Your Best Self</div>
      </div>
      <div class="photo" style="left:110px;top:220px;width:360px;height:380px;border-radius:40% 40% 12px 12px;background:linear-gradient(180deg,rgba(255,255,255,0),#9ea79a 40%,#6f786d)" role="img" aria-label="Photo of a woman meditating in a seated pose"></div>
      <div class="site abs" style="right:40px;bottom:36px">www.brightpathvitality.com</div>
    </div>
    <div class="gutter-shade"></div>
  </div>
</section>

<!-- Spread 2: method overview -->
<section class="section">
  <div class="spread">
    <div class="page page--cream">
      <div class="photo photo--round" style="left:20px;top:-110px;width:400px;height:400px;background:linear-gradient(135deg,#a97d5c,#d9d2c4 50%,#7b6a5a)" role="img" aria-label="Photo of a clinician consulting with a patient"></div>
      <div class="abs" style="left:440px;top:190px;width:20px;height:20px;border-radius:50%;background:var(--green)"></div>
      <h2 class="title abs" style="left:40px;top:310px;width:470px">The TriAxis Method: <em>Four Distinct Systems. One Complete Solution.</em></h2>
      <p class="abs" style="left:40px;top:372px;width:360px;color:var(--muted)">Each Core targets a critical area of health: Hormone Optimization, Metabolic Flexibility, Gut Health, and Lifestyle Medicine.</p>
      <div class="rail" style="left:65px;top:450px;height:170px"></div>
      <div class="item" style="left:40px;top:420px;width:340px">
        <span class="icon"><svg width="26" height="26" viewBox="0 0 24 24"><path d="M7 4c-3 0-3 6 1 6h8c4 0 4 6 0 6H9c-3 0-3 4 0 4" fill="none" stroke="var(--green)" stroke-width="2"/></svg></span>
        <div><h3>Gut Health</h3><p>This is the foundation of health. A resilient gut and well-regulated immune system support digestion, absorption and calm inflammation. Gut imbalance can drive fatigue, mood issues and hormonal disruption.</p></div>
      </div>
      <div class="rule" style="left:130px;top:560px;width:250px"></div>
      <div class="item" style="left:40px;top:590px;width:340px">
        <span class="icon"><svg width="26" height="26" viewBox="0 0 24 24"><path d="M4 12a8 8 0 0 1 14-5M20 12a8 8 0 0 1-14 5M18 3v4h-4M6 21v-4h4" fill="none" stroke="var(--green)" stroke-width="2"/></svg></span>
        <div><h3>Metabolic Flexibility</h3><p>This system controls how your body creates and uses energy. Blood sugar, blood pressure and mitochondrial function all reside here. When optimized, it supports endurance and heart health.</p></div>
      </div>
    </div>
    <div class="page page--white">
      <div class="panel" style="left:30px;top:30px;width:480px;height:270px">
        <h3>BrightPath Vitality Philosophy: A Whole-System Approach to Health</h3>
        <p>BrightPath Vitality is a modern, integrative health philosophy that prioritizes treating the root causes of imbalance, not just managing symptoms.</p>
        <p>It's built on the principle that lasting wellness comes from restoring balance across the body's interconnected systems, using a proactive approach centered on prevention and optimization.</p>
        <p><strong>At the core of this philosophy is the TriAxis Method</strong> — a framework created by BrightPath Vitality founder Dana Merrow that identifies the essential systems that govern health.</p>
      </div>
      <div class="rail" style="left:205px;top:400px;height:150px"></div>
      <div class="item" style="left:180px;top:370px;width:330px">
        <span class="icon"><svg width="26" height="26" viewBox="0 0 24 24"><path d="M12 3l7 4v8l-7 4-7-4V7z" fill="none" stroke="var(--green)" stroke-width="2"/><circle cx="12" cy="11" r="2.5" fill="var(--green)"/></svg></span>
        <div><h3>Hormone Optimization</h3><p>Hormones and neurotransmitters regulate everything from energy, mood and sleep to libido and mental clarity. Imbalance can lead to fatigue, anxiety or sexual dysfunction.</p></div>
      </div>
      <div class="rule" style="left:250px;top:500px;width:250px"></div>
      <div class="item" style="left:180px;top:530px;width:330px">
        <span class="icon"><svg width="26" height="26" viewBox="0 0 24 24"><circle cx="12" cy="5" r="2.5" fill="var(--green)"/><path d="M12 8v7M7 11h10M12 15l-4 6M12 15l4 6" fill="none" stroke="var(--green)" stroke-width="2"/></svg></span>
        <div><h3>Lifestyle Medicine</h3><p>Your ability to move, perform and recover depends on this system. Alignment, posture, injury and nutrition can lead to pain and limit physical potential.</p></div>
      </div>
    </div>
    <div class="pie-wrap">
      <div class="abs display" style="left:20px;top:52px;font-weight:700;font-size:22px">TriAxis Method<sup style="font-size:8px">™</sup></div>
      <svg class="abs" style="left:95px;top:100px" width="110" height="110" viewBox="0 0 110 110">
        <path d="M55 55V5A50 50 0 0 1 105 55Z" fill="var(--pie-yellow)"/>
        <path d="M55 55H105A50 50 0 0 1 55 105Z" fill="var(--pie-orange)"/>
        <path d="M55 55V105A50 50 0 0 1 5 55Z" fill="var(--pie-green)"/>
        <path d="M55 55H5A50 50 0 0 1 55 5Z" fill="var(--pie-blue)"/>
        <circle cx="55" cy="55" r="50" fill="none" stroke="#fff" stroke-width="2"/>
        <path d="M55 5V105M5 55H105" stroke="#fff" stroke-width="3"/>
      </svg>
      <div class="pie-label" style="left:38px;top:128px">GUT<br>HEALTH</div>
      <div class="pie-label" style="left:212px;top:110px">METABOLIC<br>FLEXIBILITY</div>
      <div class="pie-label" style="left:212px;top:190px">HORMONE<br>OPTIMIZATION</div>
      <div class="pie-label" style="left:70px;top:222px">LIFESTYLE<br>MEDICINE</div>
    </div>
    <div class="gutter-shade"></div>
  </div>
</section>

<!-- Spread 3: process -->
<section class="section">
  <div class="spread">
    <div class="page page--cream">
      <div class="photo photo--round" style="left:30px;top:20px;width:290px;height:290px;border:3px solid #fff;background:linear-gradient(135deg,#9cb4c6,#6b7784 50%,#3e4a3a)" role="img" aria-label="Photo of a mature man jogging outdoors"></div>
      <h2 class="title abs" style="left:40px;top:330px;font-size:24px">The Process</h2>
      <div class="step" style="left:40px;top:380px">
        <span class="icon icon--solid"><svg width="18" height="18" viewBox="0 0 24 24"><path d="M5 12l5 5 9-10" fill="none" stroke="#fff" stroke-width="2.5"/></svg></span>
        <p>We run 60+ advanced labs to assess your hormones, metabolic function, nutrient status, gut health and inflammation.</p>
      </div>
      <div class="step" style="left:40px;top:470px">
        <span class="icon icon--solid"><svg width="18" height="18" viewBox="0 0 24 24"><path d="M4 12h14M13 6l6 6-6 6" fill="none" stroke="#fff" stroke-width="2.5"/></svg></span>
        <p>Next, we build your custom plan including tailored supplements, prescriptions, nutrition and fitness strategies plus wearable tech for real-time feedback and daily support.</p>
      </div>
      <div class="step" style="left:285px;top:340px">
        <span class="icon icon--solid"><svg width="18" height="18" viewBox="0 0 24 24"><circle cx="12" cy="12" r="7" fill="none" stroke="#fff" stroke-width="2.5"/><path d="M12 8v4l3 2" fill="none" stroke="#fff" stroke-width="2"/></svg></span>
        <p>Then, we connect those insights to clearly show you where you are, how you got here and what to do next. You receive a report and a personal metabolic blueprint.</p>
      </div>
      <div class="step" style="left:285px;top:440px">
        <span class="icon icon--solid"><svg width="18" height="18" viewBox="0 0 24 24"><path d="M4 18l5-6 4 3 7-9" fill="none" stroke="#fff" stroke-width="2.5"/></svg></span>
        <p>This is where the shift happens. With expert coaching, regular check-ins and a plan that evolves with you, you start seeing progress: more energy, better sleep and sharper focus.</p>
      </div>
      <h3 class="abs display" style="left:285px;top:565px;font-size:18px;line-height:1.2;font-weight:700">Flexible Payment<br>Options Available</h3>
      <p class="abs" style="left:285px;top:615px;width:220px;font-size:10px">We accept HSA and FSA payments, so you can use pre-tax dollars toward your plan. We offer 12-month payment plans with no hard credit check.</p>
      <div class="book" style="left:40px;top:580px;width:200px;height:110px;background:linear-gradient(135deg,#f0a640,#d9791f)" role="img" aria-label="Image of orange printed guide books"></div>
    </div>
    <div class="page page--white">
      <h2 class="title abs" style="left:40px;top:40px;font-size:28px">The TriAxis Method:</h2>
      <p class="abs display" style="left:40px;top:82px;font-weight:700;font-size:13px;color:var(--green)">Four Distinct Systems. One Complete Solution.</p>
      <p class="abs" style="left:40px;top:104px;width:440px;font-weight:600;font-size:10px">Each Core targets a critical area of health: Hormone Optimization, Metabolic Flexibility, Gut Health, and Lifestyle Medicine.</p>
      <p class="abs" style="left:40px;top:136px;width:440px;font-size:10px;color:var(--muted)">Together, they cover every major factor influencing how you feel, age and perform, so you understand what drives your symptoms and how to fix them.</p>
      <div class="panel" style="left:30px;top:200px;width:480px;height:460px;padding-right:200px">
        <p>Where traditional medicine often divides the body into specialties, our method recognizes these systems do not operate in silos; they influence one another continuously.</p>
        <p>For example, gut dysfunction can lead to hormonal imbalances, which may contribute to metabolic slowdown, chronic pain or loss of drive and energy.</p>
        <p>BrightPath Vitality also embraces personalization, using advanced diagnostics such as metabolic testing and hormone panels to uncover patterns and design customized care plans.</p>
        <p>These plans typically include targeted nutrition, functional supplements, exercise strategies, stress regulation and gut restoration protocols.</p>
        <p>In essence, BrightPath Vitality redefines health not as the absence of disease but as optimal function across all core systems, leading to better energy, sharper focus and longer vitality.</p>
      </div>
      <div class="book" style="left:320px;top:360px;width:160px;height:120px;background:linear-gradient(135deg,#1f4c56,#163640)" role="img" aria-label="Image of teal printed guide books"></div>
    </div>
    <div class="gutter-shade"></div>
  </div>
</section>

<!-- Spread 4: FAQ -->
<section class="section">
  <div class="spread">
    <div class="page page--cream">
      <h2 class="faq-heading abs" style="left:60px;top:200px">Frequently<br><span>Asked Questions</span></h2>
      <div class="photo photo--round" style="left:-40px;top:380px;width:620px;height:620px;background:linear-gradient(135deg,#5b3e33,#c9a489 45%,#8a3a4a)" role="img" aria-label="Photo of a smiling woman talking with a friend"></div>
    </div>
    <div class="page page--white">
      <div class="panel" style="left:30px;top:30px;width:480px;height:640px">
        <div class="faq"><span class="icon"><svg width="16" height="16" viewBox="0 0 24 24"><path d="M5 12l5 5 9-10" fill="none" stroke="#fff" stroke-width="2.5"/></svg></span>
          <div><h3>What makes TriAxis different from other programs?</h3>
          <p>We don't just give you a one-size plan. Our system connects advanced labs, wearable data and expert coaching to uncover what is driving your symptoms.</p>
          <p>Most tests only check a few markers. We go deeper and give you a plan that adapts as your body changes.</p></div></div>
        <div class="faq"><span class="icon"><svg width="16" height="16" viewBox="0 0 24 24"><path d="M5 12l5 5 9-10" fill="none" stroke="#fff" stroke-width="2.5"/></svg></span>
          <div><h3>Is this covered by insurance?</h3>
          <p>We don't bill insurance directly, but many clients use HSA or FSA funds to cover labs and services. We can provide receipts for reimbursement.</p></div></div>
        <div class="faq"><span class="icon"><svg width="16" height="16" viewBox="0 0 24 24"><path d="M5 12l5 5 9-10" fill="none" stroke="#fff" stroke-width="2.5"/></svg></span>
          <div><h3>What's included in the initial assessment?</h3>
          <p>Your annual functional health audit includes:</p>
          <ul><li>Comprehensive lab testing (60+ biomarkers)</li><li>Body composition analysis</li><li>Grip strength and balance assessment</li></ul>
          <p>Your health biography connects your history, symptoms and goals.</p></div></div>
        <div class="faq"><span class="icon"><svg width="16" height="16" viewBox="0 0 24 24"><path d="M5 12l5 5 9-10" fill="none" stroke="#fff" stroke-width="2.5"/></svg></span>
          <div><h3>How long does it take to see results?</h3>
          <p>We're not here to guess or waste your time. Most clients feel real changes, more energy and better sleep, within the first 30 days, with lasting transformation in 90 days.</p></div></div>
      </div>
    </div>
    <div class="gutter-shade"></div>
  </div>
</section>

</div>
</body>
</html>
```